Landfill Gas-to-Renewable Natural Gas business

We have a website ( coralbayfuelworks .com via Net Burrow) that needs to be revamped.

We have three RNG projects in Puerto Rico (Humacao, Ponce, Salinas), that take landfill gas (LFG) and produce renewable liquid natural gas (R-LNG) for companies looking to offset their carbon emissions (footprint). We also produce a renewable carbon dioxide (R-CO2) that can be reused for industrial CO2 purposes. All CO2 is imported to the island, so reusing CO2 on the island further reduces global CO2 emissions. The design should reflect renewables, sustainability, professionalism, safety and experience in this sector.

Sites with RNG examples:
https://www.qz.com/en_us/united-states/home/what-we-do/production-and-operations/velmora-power.html
https://tidefuelplex.com/
http://brindlepower.com/operations/
https://quillgases.com/
https://www.zentorgas.com/
https://harlowgas.com/
https://pinecrestfuelworks.com/
https://stokegas.com/
https://www.vontella.com/renewable-natural-gas/
https://www.kelbyfuelsystems.com/

Industry/Entity Type

Renewables Natural Gas, Sustainability,

Coding

Coded - Design and coding required

Number of Pages Required

4 page

Requirements
Must have
• Health, Safety, Environment (HSE) aspect. Industry experience section, about us, photos, landfill gas, LNG, RNG, CO2

```html
<!DOCTYPE html>
<html lang="en">
<head>
<meta charset="utf-8">
<title>Coral Bay Fuelworks</title>
<link rel="stylesheet" href="https://fonts.googleapis.com/css2?family=Noto+Serif+Display:wght@500;600&family=Noto+Serif:wght@400;600&display=swap">
<style>
:root{
  --navy:#0b1a45;
  --navy-2:#102654;
  --blue:#1260ea;
  --green:#0bd66c;
  --ink:#1d1d2b;
  --muted:#5a5f6e;
  --line:#dfe2e8;
  --panel:#f2f3f6;
  --white:#ffffff;
}
*{box-sizing:border-box;margin:0;padding:0}
html,body{width:1200px;height:2357px;overflow:hidden}
body{position:relative;font-family:"Noto Serif",serif;color:var(--ink);background:var(--white)}
.abs{position:absolute}
.display{font-family:"Noto Serif Display",serif;font-weight:600;letter-spacing:-.5px}
.btn{position:absolute;display:flex;align-items:center;justify-content:center;border-radius:18px;color:var(--white);font-size:12px;font-weight:600}
.btn-navy{background:var(--navy)}
.btn-blue{background:var(--blue)}

/* header */
.site-header{left:0;top:0;width:1200px;height:75px;background:var(--white)}
.brand{display:flex;align-items:center;gap:10px}
.brand-dot{width:38px;height:38px;border-radius:50%;background:linear-gradient(135deg,var(--blue),var(--green))}
.brand-name{font-size:16px;line-height:16px;color:#4a5070}
.nav{left:502px;top:28px;display:flex;gap:24px;font-size:11.5px;color:var(--ink)}
.nav .active{color:var(--green);text-decoration:underline}
.icon-btn{width:30px;height:30px;border-radius:50%;background:#dfe3f3;display:flex;align-items:center;justify-content:center}

/* hero */
.hero-photo{left:0;top:75px;width:1200px;height:510px;background:linear-gradient(180deg,#3d3942 0%,#5a4f4a 45%,#3a3430 75%,#2a2623 100%)}
.hero-title{left:0;top:212px;width:1200px;text-align:center;font-size:57px;line-height:53px;color:var(--green)}
.hero-sub{left:0;top:333px;width:1200px;text-align:center;font-size:19px;line-height:25px;color:var(--white)}

/* net zero */
.nz-title{left:155px;top:666px;width:440px;text-align:center;font-size:29px;color:var(--navy)}
.nz-sub{left:155px;top:700px;width:440px;text-align:center;font-size:19px;color:var(--green);font-weight:600}
.nz-text{left:195px;top:737px;width:360px;text-align:center;font-size:13.5px;line-height:17.5px;color:#2b2d3a}
.divider{left:612px;top:681px;width:1px;height:174px;background:var(--line)}
.hse-circle{position:absolute;width:106px;height:106px;border-radius:50%;background:var(--white);box-shadow:0 4px 18px rgba(20,30,70,.09);display:flex;flex-direction:column;align-items:center;justify-content:center;gap:6px;font-size:10px;color:var(--ink)}
.hse-core{left:774px;top:720px;width:54px;height:54px;border-radius:50%;background:var(--navy);color:var(--white);display:flex;align-items:center;justify-content:center;font-size:11px;font-weight:600}

/* services */
.svc-title{left:0;top:1030px;width:1200px;text-align:center;font-size:25px;color:var(--white)}
.svc-text{left:300px;width:600px;text-align:center;font-size:10.5px;line-height:14.5px;color:#d6dbeb}
.card{position:absolute;top:1180px;width:181px;height:204px;background:var(--white);border-radius:7px;padding:3px}
.card .photo{height:154px;border-radius:6px}
.card .label{text-align:center;font-size:14px;font-weight:600;margin-top:14px;color:var(--ink)}
.card.featured{background:var(--green)}
.card.featured .label{color:var(--white)}

/* help + faq */
.help-panel{left:0;top:1523px;width:562px;height:530px;background:var(--panel)}
.sec-head{text-align:center;font-size:24px;line-height:28px;color:var(--navy)}
.field{position:absolute;left:156px;width:350px;height:34px;border:1px solid var(--line);background:var(--white);border-radius:2px;padding:9px 9px;font-size:11px;color:#9aa0ad}
.faq-item{position:absolute;left:613px;width:430px;border-top:1px solid var(--line)}
.faq-q{font-size:12.5px;font-weight:600;color:var(--blue);margin-top:16px}
.faq-toggle{position:absolute;right:16px;top:18px;width:16px;height:16px;border-radius:50%;background:var(--blue)}
.faq-a{font-size:10.5px;line-height:19px;color:var(--muted);margin-top:8px;width:410px}

/* footer */
.foot-head{font-size:12px;font-weight:600;color:var(--white);letter-spacing:.2px}
.foot-line{display:flex;gap:8px;align-items:flex-start;font-size:11px;line-height:12px;color:var(--white)}
.quick-links{font-size:11px;line-height:18px;color:var(--white)}
.quick-links .active{color:var(--green);text-decoration:underline}
.social{width:22px;height:22px;border-radius:50%;background:rgba(255,255,255,.2)}
.bottom-bar{left:0;top:2324px;width:1200px;height:33px;background:linear-gradient(90deg,var(--blue),#0aa6a8 60%,var(--green));color:var(--white);font-size:11px}
</style>
</head>
<body>

<!-- Header -->
<header class="abs site-header">
  <div class="abs brand" style="left:156px;top:12px">
    <span class="brand-dot"></span>
    <span class="brand-name">Coral Bay<br>Fuelworks</span>
  </div>
  <nav class="abs nav">
    <span class="active">Home</span><span>About Us</span><span>Services</span><span>FAQ</span><span>Contact Us</span>
  </nav>
  <div class="abs icon-btn" style="left:844px;top:22px">
    <svg width="13" height="13" viewBox="0 0 24 24"><path d="M6 2l4 4-2 3c1 3 4 6 7 7l3-2 4 4-3 4C10 21 3 14 2 5z" fill="var(--navy)"/></svg>
  </div>
  <div class="abs icon-btn" style="left:880px;top:22px">
    <svg width="12" height="10" viewBox="0 0 24 18"><rect width="24" height="18" rx="2" fill="var(--navy)"/><path d="M2 2l10 8 10-8" stroke="#dfe3f3" stroke-width="2" fill="none"/></svg>
  </div>
  <div class="btn btn-navy" style="left:929px;top:22px;width:114px;height:31px">Quick Inquiry</div>
</header>

<!-- Hero -->
<div class="abs hero-photo" role="img" aria-label="Photograph of a natural gas processing plant with towers and pipework at dusk"></div>
<svg class="abs" style="left:0;top:470px" width="1200" height="120" viewBox="0 0 1200 120">
  <defs><linearGradient id="heroWave" x1="0" x2="1"><stop offset="0" stop-color="var(--blue)"/><stop offset=".55" stop-color="#1260ea"/><stop offset="1" stop-color="var(--green)"/></linearGradient></defs>
  <path d="M0 8 C300 110 800 115 1200 10 L1200 120 L0 120Z" fill="url(#heroWave)"/>
  <path d="M0 32 C300 120 800 118 1200 30 L1200 120 L0 120Z" fill="var(--white)"/>
</svg>
<h1 class="abs display hero-title">NATURAL GAS<br>RESOURCES</h1>
<p class="abs hero-sub">See our commitment to Health, Safety,<br>Environment.</p>
<div class="btn btn-blue" style="left:546px;top:403px;width:108px;height:31px">Contact Now</div>

<!-- Net zero -->
<h2 class="abs display nz-title">ACHIEVE NET-ZERO NOW</h2>
<p class="abs nz-sub">Island Sourced Waste-to-Energy</p>
<p class="abs nz-text">Led By A Consortium Of Experienced Market Participants, Coral Bay Fuelworks Was Formed To Finance, Develop, Design, Build And Operate Environmental, Social, And Governance (ESG) Positive Energy Assets, With A Focus On Renewable Natural Gas.</p>
<div class="btn btn-navy" style="left:325px;top:840px;width:99px;height:31px">Read More</div>
<div class="abs divider"></div>

<div class="hse-circle" style="left:689px;top:660px">
  <svg width="44" height="40" viewBox="0 0 44 40"><path d="M22 38C8 28 2 20 2 12 2 6 7 2 12 2c4 0 8 2 10 6 2-4 6-6 10-6 5 0 10 4 10 10 0 8-6 16-20 26z" fill="#fbd6df" stroke="var(--navy)" stroke-width="1.6"/><path d="M6 20h9l3-6 4 12 3-8 2 2h11" stroke="#e0355a" stroke-width="1.6" fill="none"/></svg>
  <span>Health</span>
</div>
<div class="hse-circle" style="left:808px;top:660px">
  <svg width="40" height="42" viewBox="0 0 40 42"><path d="M6 22a14 14 0 0128 0z" fill="#ffd43b" stroke="var(--navy)" stroke-width="1.6"/><rect x="3" y="22" width="34" height="5" rx="2" fill="#fff" stroke="var(--navy)" stroke-width="1.6"/><path d="M9 27c0 8 5 13 11 13s11-5 11-13" fill="#fff" stroke="var(--navy)" stroke-width="1.6"/><rect x="17" y="4" width="6" height="8" fill="#ffd43b" stroke="var(--navy)" stroke-width="1.4"/></svg>
  <span>Safety</span>
</div>
<div class="hse-circle" style="left:748px;top:762px">
  <svg width="44" height="42" viewBox="0 0 44 42"><path d="M4 24a18 16 0 0036 0z" fill="var(--green)" stroke="var(--navy)" stroke-width="1.6"/><path d="M10 24h24" stroke="var(--navy)" stroke-width="1.6"/><circle cx="15" cy="12" r="6" fill="#fff" stroke="var(--navy)" stroke-width="1.6"/><circle cx="22" cy="9" r="7" fill="#fff" stroke="var(--navy)" stroke-width="1.6"/><circle cx="29" cy="12" r="6" fill="#fff" stroke="var(--navy)" stroke-width="1.6"/><path d="M22 16v8" stroke="var(--navy)" stroke-width="1.6"/></svg>
  <span>Environment</span>
</div>
<div class="abs hse-core">HSE</div>

<!-- Services -->
<svg class="abs" style="left:0;top:950px" width="1200" height="590" viewBox="0 0 1200 590" role="img" aria-label="Dark navy band over a faint industrial plant photograph">
  <defs>
    <linearGradient id="svcTop" x1="0" x2="1"><stop offset=".45" stop-color="var(--navy)"/><stop offset="1" stop-color="var(--blue)"/></linearGradient>
    <linearGradient id="svcBot" x1="0" x2="1"><stop offset="0" stop-color="var(--green)"/><stop offset=".5" stop-color="#0aa6a8"/><stop offset=".6" stop-color="var(--navy)"/></linearGradient>
  </defs>
  <path d="M0 70 C400 -10 900 -10 1200 60 L1200 480 L0 480Z" fill="url(#svcTop)"/>
  <path d="M0 70 C400 10 900 0 1200 90 L1200 510 C800 570 300 570 0 510Z" fill="var(--navy)"/>
  <path d="M0 515 C300 575 800 580 1200 505 L1200 520 C800 585 300 585 0 575Z" fill="url(#svcBot)"/>
</svg>
<h2 class="abs display svc-title">OUR SERVICES</h2>
<p class="abs svc-text" style="top:1080px">Coral Bay Fuelworks Specializes In The Development, Financing, Operation, And Management Of Complex Energy Infrastructure Projects.</p>
<p class="abs svc-text" style="top:1123px;left:290px;width:620px">We Offer A Wide Range Of Energy Management Services, Including The Design, Build, And Operation Of RNG Assets, Energy Asset Audits, Efficiency Upgrades, And More.</p>

<div class="card" style="left:200px"><div class="photo" role="img" aria-label="Cooling towers releasing steam under a cloudy sky" style="background:linear-gradient(180deg,#b9bcc0,#6e7278 60%,#3f4a3c)"></div><div class="label">Landfill Gas</div></div>
<div class="card" style="left:406px"><div class="photo" role="img" aria-label="Aerial view of LNG storage tanks at a terminal" style="background:linear-gradient(160deg,#7d6a52,#a99d8a 50%,#cfcdc6)"></div><div class="label">LNG</div></div>
<div class="card featured" style="left:613px"><div class="photo" role="img" aria-label="Steel processing columns at an RNG facility" style="background:linear-gradient(180deg,#4c5470,#8a8f9c 50%,#3a3e4c)"></div><div class="label">RNG</div></div>
<div class="card" style="left:819px"><div class="photo" role="img" aria-label="Industrial site with smokestacks releasing carbon dioxide" style="background:linear-gradient(180deg,#c9c9c4,#8d8c86 55%,#3e3d3a)"></div><div class="label">CO2</div></div>
<div class="btn btn-blue" style="left:541px;top:1420px;width:115px;height:31px">Quick Inquiry</div>

<!-- Help + FAQ -->
<div class="abs help-panel"></div>
<h2 class="abs display sec-head" style="left:156px;top:1602px;width:350px">NEED HELP? WE’RE<br>HERE FOR YOU</h2>
<div class="field" style="top:1684px">Name</div>
<div class="field" style="top:1731px">Email</div>
<div class="field" style="top:1778px">Phone</div>
<div class="field" style="top:1824px;height:91px">Message</div>
<div class="btn btn-navy" style="left:292px;top:1944px;width:78px;height:31px">Submit</div>

<h2 class="abs display sec-head" style="left:613px;top:1602px;width:430px">FREQUENTLY ASKED<br>QUESTIONS</h2>
<div class="faq-item" style="top:1684px;height:51px">
  <p class="faq-q">How are your projects financed?</p>
  <span class="faq-toggle"><svg width="16" height="16"><path d="M4 8h8M8 4v8" stroke="#fff" stroke-width="1.6"/></svg></span>
</div>
<div class="faq-item" style="top:1735px;height:130px">
  <p class="faq-q" style="color:var(--green)">How is RNG beneficial?</p>
  <span class="faq-toggle" style="background:var(--green)"><svg width="16" height="16"><path d="M4 8h8" stroke="#fff" stroke-width="1.6"/></svg></span>
  <p class="faq-a">Research shows that when all-climate benefits are considered together, RNG from dairy manure can reduce greenhouse gas emissions up to 350% when replacing traditional diesel fuel. Converting vehicles to run on net-carbon-negative RNG is a crucial lever in reducing U.S. greenhouse gas emissions.</p>
</div>
<div class="faq-item" style="top:1865px;height:51px;border-bottom:1px solid var(--line)">
  <p class="faq-q">What is biogas?</p>
  <span class="faq-toggle"><svg width="16" height="16"><path d="M4 8h8M8 4v8" stroke="#fff" stroke-width="1.6"/></svg></span>
</div>
<div class="btn btn-navy" style="left:787px;top:1944px;width:83px;height:31px">View All</div>

<!-- Footer -->
<svg class="abs" style="left:0;top:2030px" width="1200" height="294" viewBox="0 0 1200 294" role="img" aria-label="Deep blue footer band over a faint industrial plant photograph">
  <defs><linearGradient id="footBg" x1="0" y1="0" x2="0" y2="1"><stop offset="0" stop-color="#0f2456"/><stop offset="1" stop-color="#16386b"/></linearGradient></defs>
  <path d="M0 110 C400 -10 900 -15 1200 120 L1200 294 L0 294Z" fill="var(--blue)"/>
  <path d="M0 112 C400 10 900 5 1200 145 L1200 294 L0 294Z" fill="url(#footBg)"/>
</svg>
<div class="abs brand" style="left:156px;top:2150px">
  <span class="brand-dot" style="width:42px;height:42px"></span>
  <span class="brand-name" style="color:#fff;font-size:17px;line-height:18px">Coral Bay<br>Fuelworks</span>
</div>
<p class="abs foot-head" style="left:381px;top:2141px">CONTACT US</p>
<div class="abs foot-line" style="left:381px;top:2170px"><svg width="11" height="11" viewBox="0 0 24 24"><path d="M6 2l4 4-2 3c1 3 4 6 7 7l3-2 4 4-3 4C10 21 3 14 2 5z" fill="var(--green)"/></svg>+1 787-555-0142</div>
<div class="abs foot-line" style="left:381px;top:2197px"><svg width="12" height="10" viewBox="0 0 24 18"><rect width="24" height="18" rx="2" fill="var(--green)"/><path d="M2 2l10 8 10-8" stroke="#16386b" stroke-width="2" fill="none"/></svg>info@coralbayfuelworks.com</div>
<div class="abs foot-line" style="left:381px;top:2226px;width:200px"><svg width="11" height="14" viewBox="0 0 20 26" style="flex:none"><path d="M10 0a10 10 0 00-10 10c0 8 10 16 10 16s10-8 10-16A10 10 0 0010 0z" fill="var(--green)"/><circle cx="10" cy="10" r="3.5" fill="#16386b"/></svg><span>Urb. Vista Mar 118 Calle Palma, Suite 204, San Juan, Puerto Rico 00921</span></div>

<p class="abs foot-head" style="left:639px;top:2144px">QUICK LINKS</p>
<div class="abs quick-links" style="left:639px;top:2164px"><span class="active">Home</span><br>About Us<br>Services<br>FAQ<br>Contact Us</div>

<svg class="abs" style="left:794px;top:2138px" width="36" height="32" viewBox="0 0 36 32"><rect x="2" y="8" width="32" height="22" fill="none" stroke="var(--green)" stroke-width="2"/><path d="M2 8l16 13 16-13M18 2l-6 6M18 2l6 6" stroke="var(--green)" stroke-width="2" fill="none"/></svg>
<p class="abs foot-head" style="left:841px;top:2142px;line-height:14px">SUBSCRIBE TO OUR<br>NEWSLETTER</p>
<div class="abs" style="left:794px;top:2185px;width:249px;height:31px;background:#fff;border-radius:2px;font-size:10px;color:#9aa0ad;padding:9px 11px">Enter Email</div>
<svg class="abs" style="left:1020px;top:2193px" width="15" height="15" viewBox="0 0 16 16"><path d="M1 1l14 7-14 7 3-7z" fill="var(--navy)"/></svg>
<span class="abs social" style="left:797px;top:2239px"></span>
<span class="abs social" style="left:825px;top:2239px"></span>
<span class="abs social" style="left:855px;top:2239px;background:#17c3e6"></span>

<div class="abs bottom-bar">
  <span class="abs" style="left:156px;top:10px">© 2025 Coral Bay Fuelworks – All Rights Reserved.</span>
  <span class="abs" style="left:932px;top:10px">Privacy Policy</span>
</div>

</body>
</html>
```